Clean business card with logo provided

I want a card that will stand out among the masses. I need the color and image to show professionalism and yet have a family appeal showing that I only deal with win/win scenarios. The back of the card will be used to take notes about the individual so I can use that in my database entry. I like modern design but need professionalism in it also. It needs to fit my "clean, safe, and affordable housing" motto. I need to be able to write on the file and update the card details for my employees.

Target Market(s)

Investors looking to make investment income through real estate

Industry/Entity Type

Real Estate

Contact Information for Business Card

Troy Vandemark
blank address, city, st, zip code
480-555-0147
troyvandemark@quillrentals.example
www.quillrentals.example

Font styles to use
Sans Serif

Requirements
Must have
• I would like the back of the card to have lines for info. example
• Met/Visited: Date:
• Interets:
Nice to have
• I want the cards color to match the logo background color. Font with details to be san serif and black. I want the card rectangular with square corners. Standard business card size. I would like to see cards designed with both images to see which i prefer more.

```html
<!DOCTYPE html>
<html lang="en">
<head>
<meta charset="utf-8">
<title>Quill Rentals LLC – Business Card</title>
<link rel="stylesheet" href="https://fonts.googleapis.com/css2?family=Tenor+Sans&display=swap">
<style>
  :root {
    --stage: #2a2a2c;
    --card-dark: #0c0c0d;
    --card-light: #f4f4f4;
    --teal: #2bb5c9;
    --ink-light: #e6e6e6;
    --ink-dark: #111111;
    --dots: #6a6a6a;
  }
  * { box-sizing: border-box; margin: 0; padding: 0; }
  html, body { width: 1200px; height: 900px; overflow: hidden; }
  body {
    background: var(--stage);
    font-family: "Tenor Sans", "Optima", sans-serif;
    position: relative;
  }

  .card {
    position: absolute;
    width: 560px;
    height: 320px;
    box-shadow: 0 10px 30px rgba(0,0,0,.45);
  }

  .brand-name {
    color: var(--teal);
    text-transform: uppercase;
    line-height: 1;
    white-space: nowrap;
  }
  .brand-tagline { color: var(--teal); letter-spacing: .02em; white-space: nowrap; }

  /* ---------- back: notes side ---------- */
  .card--back { left: 70px; top: 60px; background: var(--card-light); }
  .back__band {
    position: absolute; left: 0; top: 24px;
    width: 210px; height: 34px; background: var(--ink-dark);
  }
  .back__brand {
    position: absolute; left: 24px; top: 70px;
    width: 240px; height: 104px; background: var(--ink-dark);
    display: flex; flex-direction: column; justify-content: center; align-items: center;
    gap: 12px;
  }
  .back__brand .brand-name { font-size: 15px; letter-spacing: .08em; }
  .back__brand .brand-tagline { font-size: 8.5px; }

  .note-field {
    position: absolute;
    display: flex; align-items: flex-end; gap: 8px;
    color: var(--teal);
    font-size: 15px;
  }
  .note-field__line {
    flex: 1; height: 0;
    border-bottom: 2px dotted var(--dots);
    margin-bottom: 4px;
  }
  .note-line {
    position: absolute; height: 0;
    border-bottom: 2px dotted var(--dots);
  }
  .field-met   { left: 290px; top: 20px; width: 245px; flex-direction: row-reverse; }
  .field-date  { left: 24px;  top: 196px; width: 280px; }
  .field-time  { left: 290px; top: 130px; width: 245px; }
  .field-int   { left: 24px;  top: 236px; width: 511px; }
  .line-1 { left: 290px; top: 62px;  width: 245px; }
  .line-2 { left: 290px; top: 96px;  width: 245px; }
  .line-3 { left: 24px;  top: 290px; width: 511px; }

  /* ---------- front: contact side ---------- */
  .card--front { left: 570px; top: 520px; background: var(--card-dark); }
  .front__contacts {
    position: absolute; right: 26px; top: 34px;
    list-style: none; text-align: right;
  }
  .front__contacts li {
    color: var(--ink-light); font-size: 14.5px; line-height: 25px;
    display: flex; justify-content: flex-end; align-items: center; gap: 8px;
  }
  .icon { width: 12px; height: 12px; fill: var(--teal); flex: none; }
  .front__rule {
    position: absolute; left: 250px; right: 0; top: 122px;
    height: 1px; background: var(--teal);
  }
  .front__person { position: absolute; left: 30px; top: 142px; }
  .person-name {
    color: var(--teal); font-size: 26px; letter-spacing: .02em;
    font-weight: 400; text-transform: uppercase; white-space: nowrap;
  }
  .person-phone {
    margin-top: 10px; color: var(--ink-light); font-size: 17px;
    display: flex; align-items: center; gap: 10px;
  }
  .front__brand {
    position: absolute; right: 26px; top: 236px; text-align: right;
  }
  .front__brand .brand-name { font-size: 22px; letter-spacing: .1em; }
  .front__brand .brand-tagline { font-size: 11px; margin-top: 10px; }
</style>
</head>
<body>

  <section class="card card--back" aria-label="Card back: meeting notes">
    <div class="back__band"></div>
    <div class="back__brand">
      <span class="brand-name">Quill Rentals LLC</span>
      <span class="brand-tagline">Providing clean, safe, and affordable housing</span>
    </div>

    <div class="note-field field-met"><span>Met/Visited :</span><span class="note-field__line"></span></div>
    <div class="note-line line-1"></div>
    <div class="note-line line-2"></div>
    <div class="note-field field-time"><span>Time:</span><span class="note-field__line"></span></div>
    <div class="note-field field-date"><span>Date:</span><span class="note-field__line"></span></div>
    <div class="note-field field-int"><span>INTERETS :</span><span class="note-field__line"></span></div>
    <div class="note-line line-3"></div>
  </section>

  <section class="card card--front" aria-label="Card front: contact details">
    <ul class="front__contacts">
      <li>www.quillrentals.example
        <svg class="icon" viewBox="0 0 12 12"><circle cx="6" cy="6" r="5.5"/></svg></li>
      <li>troyvandemark@quillrentals.example
        <svg class="icon" viewBox="0 0 12 12"><rect x="0.5" y="2.5" width="11" height="7" rx="1"/></svg></li>
      <li>blank address, city, st, zip code
        <svg class="icon" viewBox="0 0 12 12"><path d="M6 0a4 4 0 0 1 4 4c0 3-4 8-4 8S2 7 2 4a4 4 0 0 1 4-4zm0 2.5a1.5 1.5 0 1 0 0 3 1.5 1.5 0 0 0 0-3z"/></svg></li>
    </ul>
    <div class="front__rule"></div>

    <div class="front__person">
      <h1 class="person-name">Troy Vandemark</h1>
      <p class="person-phone">
        <svg class="icon" viewBox="0 0 12 12"><path d="M2.5 0.5l2 2-1 1.5c.7 1.5 1.8 2.6 3.5 3.5l1.5-1 2 2-1.5 2C4.5 10.5 1.5 7.5.5 2z"/></svg>
        480-555-0147
      </p>
    </div>

    <div class="front__brand">
      <div class="brand-name">Quill Rentals LLC</div>
      <div class="brand-tagline">Providing clean, safe, and affordable housing</div>
    </div>
  </section>

</body>
</html>
```